Church needs an introductory/informative postcard

We are looking for a postcard that would introduce our church along with having our programing information. We need it to be in Spanish, I can provide the necessary translation. Please provide us with ideas for a tag line that invites people to come check us out. We can provide a bible scripture if necessary, but would like something short that projects interest and confidence. We have a logo that we would like incorporated.

Target Market(s)

Hispanic

Industry/Entity Type

Religious

Requirements
Must have
• Colorful to coordinate with our logo so it flows well
• Have an tag line that invites people to our church
Nice to have
• have a modern feel
• if needed we can provide some pictures of our building
Should not have
• Pictures of people

```html
<!DOCTYPE html>
<html lang="es">
<head>
<meta charset="utf-8">
<title>Postal Iglesia Casa de Luz</title>
<link href="https://fonts.googleapis.com/css2?family=Bebas+Neue&family=Lato:wght@400;700;900&family=Oswald:wght@500&family=PT+Serif:wght@700&display=swap" rel="stylesheet">
<style>
  :root{
    --bg:#e9e9ea;
    --ink:#3d3d3f;
    --orange:#f15a29;
    --purple:#5b2d8e;
    --green:#8cc63f;
    --blue:#29abe2;
    --sky-top:#dfe6f3;
    --sky-low:#f7f8fc;
    --white:#ffffff;
    --text:#222222;
    --rule:#9a9a9a;
    --stamp:#eeeeee;
    --label:#555555;
  }
  *{margin:0;padding:0;box-sizing:border-box}
  html,body{width:902px;height:1200px;overflow:hidden;background:var(--bg)}
  body{position:relative;font-family:'Lato',sans-serif}

  .side-label{position:absolute;font-family:'Lato',sans-serif;font-weight:700;font-size:28px;color:var(--label);letter-spacing:1px}
  .side-label--front{left:312px;top:22px}
  .side-label--back{left:492px;top:1150px}

  .card{position:absolute;overflow:hidden;box-shadow:0 3px 10px rgba(0,0,0,.25)}
  .card svg.card-art{position:absolute;left:0;top:0}

  /* FRONT */
  .card--front{left:40px;top:72px;width:675px;height:525px;background:var(--sky-low)}
  .headline{position:absolute;left:28px;top:30px;font-family:'Bebas Neue',sans-serif;font-size:78px;line-height:.98;letter-spacing:.5px}
  .headline__top{color:var(--ink);display:block}
  .headline__bottom{color:var(--orange);display:block}
  .brand{position:absolute;display:flex;align-items:center;gap:8px}
  .brand__dot{width:16px;height:16px;border-radius:50%;background:var(--orange)}
  .brand__name{font-family:'Lato',sans-serif;font-weight:700;color:var(--purple);letter-spacing:1.5px}
  .card--front .brand{left:42px;top:316px}
  .card--front .brand__name{font-size:22px}
  .front-contact{position:absolute;left:30px;top:420px;color:var(--white);font-size:13.5px;line-height:17px}
  .contact-row{display:flex;align-items:flex-start;gap:8px}
  .contact-row svg{flex:none;margin-top:2px}
  .contact-name{color:var(--orange);font-weight:900}
  .front-contact .web{margin-top:8px;font-weight:700}

  /* BACK */
  .card--back{left:207px;top:626px;width:673px;height:522px;background:var(--white)}
  .schedule-title{position:absolute;left:17px;top:27px;font-family:'Oswald',sans-serif;font-weight:500;font-size:21px;color:var(--purple);transform:scaleX(.88);transform-origin:left}
  .service{position:absolute;left:15px;width:315px;display:flex;gap:12px}
  .service__photo{flex:none;width:74px;height:74px;border-radius:50%;border:3px solid var(--orange);background:var(--white);padding:2px}
  .service__photo span{display:block;width:100%;height:100%;border-radius:50%}
  .service__title{font-family:'PT Serif',serif;font-weight:700;font-size:17px;color:var(--orange);line-height:20px}
  .service__text{font-size:9.3px;line-height:12px;color:var(--text);text-align:justify}
  .service--sun{top:76px}
  .service--wed{top:172px}
  .service--mon{top:270px}
  .photo-worship{background:radial-gradient(circle at 50% 35%,#f4e2c4,#8a6a4c 60%,#3a2a20)}
  .photo-study{background:radial-gradient(circle at 50% 50%,#3a3a3a,#b07a66 55%,#e2a795)}
  .photo-prayer{background:radial-gradient(circle at 50% 50%,#c47a4c,#6b3418 60%,#1e0c05)}
  .back-contact{position:absolute;left:18px;top:376px;font-size:13px;line-height:16px;color:var(--white)}
  .back-contact .contact-name{color:var(--purple)}
  .back-web{position:absolute;left:18px;top:436px;font-size:11.5px;color:var(--white);font-weight:700;display:flex;gap:8px;align-items:center}
  .back-web .visit{color:var(--green)}
  .card--back .brand{left:368px;top:52px}
  .card--back .brand__name{font-size:16px}
  .stamp-box{position:absolute;left:543px;top:29px;width:103px;height:105px;background:var(--stamp)}
  .address-line{position:absolute;left:406px;width:240px;height:1px;background:var(--rule)}
</style>
</head>
<body>

<div class="side-label side-label--front">FRONT</div>

<section class="card card--front">
  <svg class="card-art" width="675" height="525" viewBox="0 0 675 525" aria-hidden="true">
    <defs>
      <linearGradient id="sky" x1="0" y1="0" x2="0" y2="1">
        <stop offset="0" stop-color="#d8e0f0"/>
        <stop offset="1" stop-color="#f8f9fc"/>
      </linearGradient>
      <linearGradient id="building" x1="0" y1="0" x2="0" y2="1">
        <stop offset="0" stop-color="#3f7fd0"/>
        <stop offset=".35" stop-color="#e8eaec"/>
        <stop offset=".75" stop-color="#d9d6cf"/>
        <stop offset="1" stop-color="#c79a72"/>
      </linearGradient>
    </defs>
    <rect width="675" height="525" fill="url(#sky)"/>
    <!-- bottom-left bands -->
    <path d="M0 385 C120 360 240 365 330 400 L330 525 L0 525 Z" fill="var(--green)"/>
    <path d="M0 395 C120 372 240 378 330 412 L330 525 L0 525 Z" fill="var(--blue)"/>
    <path d="M0 405 C120 385 240 392 330 430 L330 525 L0 525 Z" fill="var(--purple)"/>
    <!-- heart-curve frame bands -->
    <g transform="translate(-30,0)">
      <path d="M500 525 C330 440 230 300 320 230 C380 185 460 200 500 225 C490 130 530 30 640 0 L705 0 L705 525 Z" fill="var(--purple)"/>
    </g>
    <g transform="translate(-17,0)">
      <path d="M500 525 C330 440 230 300 320 230 C380 185 460 200 500 225 C490 130 530 30 640 0 L705 0 L705 525 Z" fill="var(--orange)"/>
    </g>
    <g transform="translate(-6,0)">
      <path d="M500 525 C330 440 230 300 320 230 C380 185 460 200 500 225 C490 130 530 30 640 0 L705 0 L705 525 Z" fill="var(--white)"/>
    </g>
    <path role="img" aria-label="Photo of the white church building with arched doorway and lamp post" d="M500 525 C330 440 230 300 320 230 C380 185 460 200 500 225 C490 130 530 30 640 0 L705 0 L705 525 Z" fill="url(#building)"/>
  </svg>

  <h1 class="headline">
    <span class="headline__top">GOD'S BLESSINGS</span>
    <span class="headline__bottom">GIVEN OUT HERE !</span>
  </h1>

  <div class="brand">
    <span class="brand__dot"></span>
    <span class="brand__name">CASA DE LUZ</span>
  </div>

  <div class="front-contact">
    <div class="contact-row">
      <svg width="10" height="13" viewBox="0 0 10 13"><path d="M5 0a5 5 0 0 0-5 5c0 4 5 8 5 8s5-4 5-8a5 5 0 0 0-5-5zm0 7a2 2 0 1 1 0-4 2 2 0 0 1 0 4z" fill="var(--green)"/></svg>
      <div><span class="contact-name">IGLESIA CASA DE LUZ</span><br>2450 Alameda Ave.<br>Riverton, TX 75099</div>
    </div>
    <div class="contact-row web">
      <svg width="11" height="11" viewBox="0 0 12 12"><circle cx="6" cy="6" r="5.3" fill="none" stroke="var(--green)" stroke-width="1.3"/><path d="M.7 6h10.6M6 .7c-3 3-3 7.6 0 10.6M6 .7c3 3 3 7.6 0 10.6" fill="none" stroke="var(--green)" stroke-width="1"/></svg>
      <span>www.iglesiacasadeluz.org</span>
    </div>
  </div>
</section>

<section class="card card--back">
  <svg class="card-art" width="673" height="522" viewBox="0 0 673 522" aria-hidden="true">
    <defs>
      <linearGradient id="panel" x1="0" y1="0" x2="1" y2="1">
        <stop offset="0" stop-color="#e9eef8"/>
        <stop offset="1" stop-color="#f6f8fc"/>
      </linearGradient>
    </defs>
    <path d="M0 0 L300 0 C420 60 390 330 255 430 L0 430 Z" fill="url(#panel)"/>
    <path d="M322 78 C380 170 370 360 250 456 L285 456 C395 360 390 175 342 90 Z" fill="var(--orange)"/>
    <path d="M322 78 C370 170 355 350 240 456 L262 456 C372 355 372 170 333 84 Z" fill="var(--purple)"/>
    <path d="M0 367 L270 367 C255 392 240 412 222 432 L0 432 Z" fill="var(--green)"/>
    <rect x="0" y="432" width="285" height="24" fill="var(--purple)"/>
  </svg>

  <h2 class="schedule-title">HORARIO DE SERVICIOS</h2>

  <div class="service service--sun">
    <div class="service__photo"><span class="photo-worship" role="img" aria-label="Photo of a worship service before a lit cross"></span></div>
    <div>
      <h3 class="service__title">DOMINGO 10 AM</h3>
      <p class="service__text">Nos reunimos los domingos a las diez de la mañana para celebrar un servicio de alabanza y adoración a nuestro Dios con una predicación enfocada en la palabra de Dios.</p>
    </div>
  </div>

  <div class="service service--wed">
    <div class="service__photo"><span class="photo-study" role="img" aria-label="Photo of hands gathered around an open bible"></span></div>
    <div>
      <h3 class="service__title">MIERCOLES 7 PM</h3>
      <p class="service__text">Los miercoles tenemos estudios bíblicos para toda la familia basados en una teologia pentecostal cristiana con el fin de alimentar nuestro crecimiento en el conocimiento de Dios</p>
    </div>
  </div>

  <div class="service service--mon">
    <div class="service__photo"><span class="photo-prayer" role="img" aria-label="Photo of hands folded in prayer"></span></div>
    <div>
      <h3 class="service__title">LUNES 7 PM</h3>
      <p class="service__text">Todos los lunes a las siete de la noche nos reunimos para un servicio de oración y adoración uniéndonos para clamar a Dios y buscar su voluntad para nuestras vidas.</p>
    </div>
  </div>

  <div class="back-contact contact-row">
    <svg width="10" height="13" viewBox="0 0 10 13"><path d="M5 0a5 5 0 0 0-5 5c0 4 5 8 5 8s5-4 5-8a5 5 0 0 0-5-5zm0 7a2 2 0 1 1 0-4 2 2 0 0 1 0 4z" fill="var(--orange)"/></svg>
    <div><span class="contact-name">IGLESIA CASA DE LUZ</span><br>2450 Alameda Ave.<br>Riverton, TX 75099</div>
  </div>

  <div class="back-web">
    <svg width="11" height="11" viewBox="0 0 12 12"><circle cx="6" cy="6" r="5.3" fill="none" stroke="var(--orange)" stroke-width="1.3"/><path d="M.7 6h10.6M6 .7c-3 3-3 7.6 0 10.6M6 .7c3 3 3 7.6 0 10.6" fill="none" stroke="var(--orange)" stroke-width="1"/></svg>
    <span class="visit">Visit Us :</span>
    <span>www.iglesiacasadeluz.org</span>
  </div>

  <div class="brand">
    <span class="brand__dot"></span>
    <span class="brand__name">CASA DE LUZ</span>
  </div>

  <div class="stamp-box"></div>
  <div class="address-line" style="top:241px"></div>
  <div class="address-line" style="top:282px"></div>
  <div class="address-line" style="top:324px"></div>
</section>

<div class="side-label side-label--back">BACK</div>

</body>
</html>
```